Company brochure for our unique consulting business

We are a small consulting business offering a unique set of services to our clients.. In simple terms we are a business improvement consultancy helping our clients get the best out of their businesses. We work with clients across multiple sectors and deliver a variety of services. We want to put together a brochure to cover these main themes:1. Who we are2. What we do3. The type of people we employ4. The sectors we work inWhile the brochure needs to have a certain corporate feel to it, we don't want it to be "boring" or "stiff". We would like it to have a slightly "friendly" or "informal" feel to it, to reflect the type of organisation we are.We have a company website http://tollandvergeadvisory.com , however we do not want to directly replicate the content or feel as we recognise it needs updating.We would like the brochure to be A4 portrait format. We anticipate requiring 12 sides (including covers) but we are happy to be guided on this based on the content we have provided.The attached ppt file gives the detail of the content to be included and also shows the proposed pagination. For the front cover we would like to try 2 versions, one with the TVA logo and one with the Tolland Verge Advisory logo (a file of both is attached)One of the most important pages will be the "Our Services" page. We would like this to cover the centre fold. In the ppt file we have shown an example layout, but this is where we need most help - we are clearly not graphic designers! This page will be the most used page in sales meetings etc.Also attached is the following:1. file for our TollandVerge Advisory company logo.2. File for our TVA company logo3. Files for Derek's signatures (for under photos) - Owen's to follow4. Photo of Derek & Owen (person in purple shirt to be cropped out)Thank you and really excited to see what everyone comes back with.Derek & Owen

Target Market(s)

Very broad - Manufacturing, Healthcare, Hospitality

Industry/Entity Type

Management Consulting

Font styles to use
Other font styles liked:
• We use Swiss721, but happy to be guided by designer

Colors
3276b5
85abd2
0355a3
333333
5c5c5c
9d9d9d
d9d9d9

Requirements
Must have
• Corporate feel
Nice to have
• Slightly friendly feel
• Our standard "blue" is (CORRECTION) - R55 G96 B146 #376092 and our standard grey is R197 G178, B179 - #B3B2B2, which we would like to keep, but other colours we are happy to be guided on. Brand guidelines attached.

```html
<!DOCTYPE html>
<html lang="en">
<head>
<meta charset="utf-8">
<title>Tolland Verge Advisory – Brochure Covers</title>
<link href="https://fonts.googleapis.com/css2?family=Open+Sans:wght@300;400;600;700&display=swap" rel="stylesheet">
<style>
  :root {
    --backdrop: #e4e4e4;
    --paper: #ffffff;
    --paper-shade: #f6f6f6;
    --brand-blue: #335c8f;
    --accent-green: #4a9a36;
    --accent-gold: #b9923a;
    --claret: #8e1d22;
    --claret-soft: #c48a8c;
    --ink: #333333;
    --logo-ink: #1c1c1c;
  }
  * { box-sizing: border-box; margin: 0; padding: 0; }
  html, body { width: 1200px; height: 960px; overflow: hidden; }
  body {
    background: var(--backdrop);
    font-family: "Open Sans", Arial, sans-serif;
    position: relative;
  }
  .spread {
    position: absolute;
    left: 50px; top: 91px;
    width: 1100px; height: 778px;
    background: var(--paper);
    box-shadow: 0 6px 24px rgba(0,0,0,.12);
  }
  .page { position: absolute; top: 0; height: 100%; width: 550px; }
  .page--back { left: 0; background: linear-gradient(90deg, var(--paper) 80%, var(--paper-shade)); }
  .page--front { left: 550px; background: var(--paper-shade); }

  .contact {
    position: absolute; left: 80px; top: 610px;
    display: flex; gap: 40px;
    font-size: 10px; line-height: 1.45; color: var(--ink);
    font-style: normal;
  }
  .contact strong { font-weight: 700; }

  .cover-band {
    position: absolute; left: 0; top: 0;
    width: 550px; height: 340px;
    background: var(--brand-blue);
  }
  .tagline {
    position: absolute; left: 60px; top: 160px;
    color: #fff; font-size: 12px; letter-spacing: .04em; font-weight: 400;
  }
  .hero {
    position: absolute; left: 490px; top: 210px;
    width: 370px; height: 280px;
  }
  .hero__photo {
    position: absolute; top: 0; bottom: 0; left: 12px; right: 16px;
    background: linear-gradient(135deg, #c9b49c 0%, #e4cdb5 35%, #b7a592 65%, #8f8a86 100%);
  }
  .hero__bar-left {
    position: absolute; left: 0; top: 0; width: 12px; height: 100%;
    background: var(--accent-green);
  }
  .hero__bar-right {
    position: absolute; right: 0; top: 0; width: 16px; height: 100%;
    background: linear-gradient(180deg, var(--accent-green), var(--accent-gold) 45%, var(--accent-gold));
  }
  .brand-name {
    position: absolute; right: 24px; top: 380px;
    font-size: 18px; font-weight: 600; color: var(--logo-ink); letter-spacing: -.01em;
  }
  .strapline {
    position: absolute; left: 160px; top: 540px;
    color: var(--claret); font-size: 20px; line-height: 1.15; font-weight: 400;
  }
  .strapline .light { font-weight: 300; }
  .web {
    position: absolute; left: 160px; top: 602px;
    color: var(--claret-soft); font-size: 11px;
  }
</style>
</head>
<body>
  <div class="spread">
    <section class="page page--back">
      <address class="contact">
        <div class="contact__address">
          <strong>TVA Limited</strong><br>
          Kestrel Chambers<br>
          Mill Lane<br>
          Ashbury<br>
          AB1 2CD
        </div>
        <div class="contact__lines">
          Tel: +44 (0) 1632 960451<br>
          enquiries@tollandvergegroup.com<br>
          www.tollandvergegroup.com
        </div>
      </address>
    </section>

    <section class="page page--front">
      <div class="cover-band"></div>
      <p class="tagline">BETTER PEOPLE, BETTER BUSINESS</p>
      <p class="brand-name">Tolland Verge Advisory</p>
      <p class="strapline">business improvement<br>by tollandverge<span class="light">advisory</span></p>
      <p class="web">tollandvergeadvisory.com</p>
    </section>

    <div class="hero">
      <div class="hero__bar-left"></div>
      <div class="hero__photo" role="img" aria-label="Photograph of a smiling team of colleagues gathered around a desk in a bright office"></div>
      <div class="hero__bar-right"></div>
    </div>
  </div>
</body>
</html>
```